New Business Card

We need to refresh our business cards. We designed these ourselves and we have no graphic design experience. We would like to find a new business card design that is professional and unique. We are an auto finance company. Feel free to play with the logo, but we would like to keep the eye very present on the card. Our corporate colors are green, grey, and white.
Green - RGB - 168,215,27; HEX - #AADD22
Grey - RGB - 196,196,196; HEX - #C4C4C4
Updates
Need to upload the vector file to finalize the project. The last logo was for a jpeg that didn't stretch well.
Industry/Entity Type
Financial Service
Contact Information for Business Card
Honestly don't know...I need your help!

```html
<!DOCTYPE html>
<html lang="en">
<head>
<meta charset="utf-8">
<title>Brightlook – Business Card</title>
<link rel="stylesheet" href="https://fonts.googleapis.com/css2?family=Cagliostro&display=swap">
<style>
  :root {
    --brand-green: #aad13c;
    --brand-grey: #c4c4c4;
    --text-grey: #b4b4b4;
    --paper: #ffffff;
    --backdrop: #383838;
  }
  * { margin: 0; padding: 0; box-sizing: border-box; }
  html, body {
    width: 1001px;
    height: 1200px;
    overflow: hidden;
    background: var(--backdrop);
    font-family: "Cagliostro", sans-serif;
  }
  .sheet {
    position: relative;
    width: 1001px;
    height: 1200px;
  }
  .card {
    position: absolute;
    left: 10px;
    width: 981px;
    background: var(--paper);
  }
  .card--front { top: 7px; height: 561px; }
  .card--back { top: 628px; height: 562px; }
  .card__frame {
    position: absolute;
    left: 34px;
    top: 36px;
    width: 910px;
    height: 491px;
    border: 3px solid var(--brand-grey);
  }
  .card--back .card__frame { top: 35px; }

  .brand {
    position: absolute;
    left: 0;
    right: 0;
    top: 100px;
    text-align: center;
  }
  .brand__dot {
    display: block;
    width: 150px;
    height: 150px;
    margin: 0 auto;
    border-radius: 50%;
    background: var(--brand-green);
  }
  .brand__name {
    display: block;
    margin-top: 12px;
    font-size: 97px;
    line-height: 1;
    color: var(--brand-green);
    font-weight: 400;
  }

  .identity {
    position: absolute;
    right: 90px;
    top: 92px;
    text-align: right;
  }
  .identity__name {
    font-size: 64px;
    line-height: 1;
    color: var(--brand-green);
    font-weight: 400;
    text-transform: uppercase;
    letter-spacing: 2px;
  }
  .identity__role {
    margin-top: 24px;
    margin-right: -7px;
    font-size: 23px;
    letter-spacing: 7px;
    color: var(--text-grey);
    text-transform: uppercase;
  }

  .contacts {
    position: absolute;
    left: 80px;
    top: 327px;
    display: grid;
    grid-template-columns: 170px auto;
    row-gap: 1px;
    font-size: 26px;
    line-height: 32px;
    color: var(--text-grey);
    letter-spacing: 1px;
  }
</style>
</head>
<body>
<main class="sheet">
  <section class="card card--front">
    <div class="card__frame"></div>
    <div class="brand">
      <span class="brand__dot"></span>
      <span class="brand__name">Brightlook</span>
    </div>
  </section>

  <section class="card card--back">
    <div class="card__frame"></div>
    <div class="identity">
      <h1 class="identity__name">Mark Ellis</h1>
      <p class="identity__role">Sales Consultant</p>
    </div>
    <dl class="contacts">
      <dt>Mob:</dt><dd>021 555 0192</dd>
      <dt>Tel:</dt><dd>04 555 0178</dd>
      <dt>E-mail:</dt><dd>mark@brightlook.com</dd>
      <dt>Website:</dt><dd>www.brightlookcapital.com</dd>
    </dl>
  </section>
</main>
</body>
</html>
```